Marrowgate Auctions Business Cards Design Needed

I need a business card design that is modern looking - double sided (maybe just my logo on the back, but open to suggestions) - the overall design is up to you. I want it to be easy to read - not over the top flashy. I already have a company logo which I uploaded so that needs to be used. The colors of my logo are the colors I want on the card... so blue and gray (do need to match the logo colors).

Requirements
Must have
• Would like the card to be sleek, modern and easy to ready

```html
<!DOCTYPE html>
<html lang="en">
<head>
<meta charset="utf-8">
<title>Marrowgate Auctions – Business Card</title>
<link href="https://fonts.googleapis.com/css2?family=Roboto:wght@400;500&family=Saira:wght@600;700&display=swap" rel="stylesheet">
<style>
  :root {
    --brand-blue: #1f6fb2;
    --divider-blue: #2a74b8;
    --ink: #3a3b3d;
    --ink-soft: #55575a;
    --card-dark: #424345;
    --card-dark-edge: #38393b;
    --logo-gray: #c9cacc;
    --tag-gray: #555658;
    --stage: #2b2c2e;
    --paper: #ffffff;
    --paper-shade: #ececec;
  }
  * { margin: 0; padding: 0; box-sizing: border-box; }
  html, body { width: 1200px; height: 900px; overflow: hidden; }
  body {
    background: var(--stage);
    display: flex;
    flex-direction: column;
    align-items: center;
    justify-content: center;
    gap: 44px;
    font-family: "Roboto", Arial, sans-serif;
  }
  .card {
    position: relative;
    width: 630px;
    height: 360px;
    border-radius: 18px;
    overflow: hidden;
    box-shadow: 0 14px 30px rgba(0,0,0,.45);
  }

  /* Front */
  .card-front {
    background: radial-gradient(ellipse at 55% 45%, var(--paper) 40%, var(--paper-shade) 100%);
  }
  .identity {
    position: absolute;
    left: 0;
    top: 112px;
    width: 292px;
    text-align: right;
  }
  .identity-name {
    font-family: "Saira", Arial, sans-serif;
    font-weight: 700;
    font-size: 34px;
    letter-spacing: 1px;
    color: var(--brand-blue);
    line-height: 1;
  }
  .identity-title {
    margin-top: 8px;
    font-size: 15px;
    color: var(--ink-soft);
    letter-spacing: .3px;
  }
  .divider {
    position: absolute;
    left: 312px;
    top: 104px;
    width: 2px;
    height: 78px;
    background: var(--divider-blue);
  }
  .contact-list {
    position: absolute;
    left: 334px;
    top: 104px;
    list-style: none;
  }
  .contact-item {
    display: flex;
    align-items: center;
    gap: 9px;
    font-size: 15px;
    color: var(--ink);
    line-height: 26px;
    letter-spacing: .2px;
  }
  .contact-icon { width: 12px; height: 12px; fill: var(--brand-blue); flex: none; }
  .location-tab {
    position: absolute;
    left: 222px;
    bottom: 0;
    width: 186px;
    height: 40px;
    background: var(--tag-gray);
    color: #f2f2f2;
    font-size: 16px;
    letter-spacing: .5px;
    display: flex;
    align-items: center;
    justify-content: center;
  }

  /* Back */
  .card-back {
    background: linear-gradient(160deg, var(--card-dark) 0%, var(--card-dark-edge) 100%);
    display: flex;
    flex-direction: column;
    align-items: center;
    justify-content: center;
  }
  .brand-name {
    display: flex;
    align-items: center;
    gap: 14px;
    font-family: "Saira", Arial, sans-serif;
    font-weight: 700;
    font-size: 40px;
    letter-spacing: 1.5px;
    color: var(--logo-gray);
    text-transform: uppercase;
    line-height: 1;
  }
  .brand-mark {
    width: 30px;
    height: 30px;
    background: var(--brand-blue);
    flex: none;
  }
  .brand-tagline {
    margin-top: 20px;
    font-family: "Saira", Arial, sans-serif;
    font-weight: 600;
    font-size: 15px;
    letter-spacing: 2px;
    color: var(--logo-gray);
    text-transform: uppercase;
  }
</style>
</head>
<body>

  <section class="card card-front" aria-label="Business card front">
    <div class="identity">
      <h1 class="identity-name">ROWAN PELL</h1>
      <p class="identity-title">Owner/President - Auctioneer</p>
    </div>
    <div class="divider"></div>
    <ul class="contact-list">
      <li class="contact-item">
        <svg class="contact-icon" viewBox="0 0 24 24" aria-hidden="true"><path d="M6.6 10.8a15.1 15.1 0 0 0 6.6 6.6l2.2-2.2c.3-.3.7-.4 1-.2 1.1.4 2.3.6 3.6.6.6 0 1 .4 1 1V20c0 .6-.4 1-1 1A17 17 0 0 1 3 4c0-.6.4-1 1-1h3.5c.6 0 1 .4 1 1 0 1.3.2 2.5.6 3.6.1.3 0 .7-.2 1z"/></svg>
        702-555-0148
      </li>
      <li class="contact-item">
        <svg class="contact-icon" viewBox="0 0 24 24" aria-hidden="true"><path d="M2 5h20v14H2zm2 2v.5l8 5 8-5V7zm0 2.8V17h16V9.8l-8 5z"/></svg>
        hello@marrowgateauctions.com
      </li>
      <li class="contact-item">
        <svg class="contact-icon" viewBox="0 0 24 24" aria-hidden="true"><path d="M12 2a10 10 0 1 0 0 20 10 10 0 0 0 0-20zm6.9 6h-2.9a15 15 0 0 0-1.4-3.8A8 8 0 0 1 18.9 8zM12 4c.8 1.2 1.5 2.5 1.9 4h-3.8c.4-1.5 1.1-2.8 1.9-4zM4.3 14a8 8 0 0 1 0-4h3.4a16 16 0 0 0 0 4zm.8 2h2.9c.3 1.4.8 2.7 1.4 3.8A8 8 0 0 1 5.1 16zM8 8H5.1a8 8 0 0 1 4.3-3.8C8.8 5.3 8.3 6.6 8 8zm4 12c-.8-1.2-1.5-2.5-1.9-4h3.8c-.4 1.5-1.1 2.8-1.9 4zm2.3-6H9.7a14 14 0 0 1 0-4h4.6a14 14 0 0 1 0 4zm.3 5.8c.6-1.1 1.1-2.4 1.4-3.8h2.9a8 8 0 0 1-4.3 3.8zm1.7-5.8a16 16 0 0 0 0-4h3.4a8 8 0 0 1 0 4z"/></svg>
        www.bidrevival.com
      </li>
    </ul>
    <div class="location-tab">Cedar Hollow, WA</div>
  </section>

  <section class="card card-back" aria-label="Business card back">
    <div class="brand-name"><span class="brand-mark"></span>Marrowgate Auctions</div>
    <p class="brand-tagline">Smarter Benefit Auctions Coast to Coast</p>
  </section>

</body>
</html>
```